Digital marketing agency needs a new website design

We need a new responsive design for our website: https://brivolta.com/

Brivolta is a french digital marketing company who specializes in helping companies rank higher on Quendo search engine for their keywords in order to be more visible and have more traffic and clients.

I need you to design these 5 pages:
- Home page: https://brivolta.com
- Pricing page: https://brivolta.com/packs-backlinks/
- Contact page: https://brivolta.com/contact/
- Thank you page: https://brivolta.com/merci-temp/
- Simple page : https://brivolta.com/a-propos/

Here is a list of websites that we like their design. Use it for inspiration, but make sure it is different :

https://fenrolt.io/ (this is the one I like the most)
https://ubro.com/
http://www.garvelnest.com/
https://lumbardeau.fr/
https://www.tressaplank.com/home
https://dovermick.com/fr/
https://kalvoxa.io/
https://tramoisenet.fr/

I want a 75% color background and 25% white. You should use many bright/pastel colors like this website : https://fenrolt.io/

Keep the contact form in the website header.

Target Market(s)

small business owners

Industry/Entity Type

Digital Marketing

Number of Pages Required

5+ page

Font styles to use
Sans Serif

Colors

Designer to choose colors to be used in the design.

Requirements
Must have
• Contact form in header.
• Prominent call-to-action buttons.
• Use of at least 1 flashy color, possible to use many.
• Keep the 3 chart images.
• Keep client testimonials

```html
<!DOCTYPE html>
<html lang="en">
<head>
<meta charset="utf-8">
<title>Brivolta — French Backlinks on Quality Magazines and Blogs</title>
<link rel="stylesheet" href="https://fonts.googleapis.com/css2?family=ABeeZee&family=Montserrat:wght@400;500;600;700&display=swap">
<style>
  :root {
    --ink: #1d1d24;
    --muted: #6b6b75;
    --pink: #ff3366;
    --pink-soft: #f06a98;
    --lavender: #c7a7d6;
    --sky: #8ecbf4;
    --blue: #1fa4f4;
    --teal: #2ec4ae;
    --white: #ffffff;
    --line: #e3e3e8;
    --link: #1a9fe0;
    --heading: 'ABeeZee', sans-serif;
    --body: 'Montserrat', sans-serif;
  }
  * { box-sizing: border-box; margin: 0; padding: 0; }
  html, body { width: 1200px; height: 3358px; overflow: hidden; }
  body { position: relative; background: var(--white); font-family: var(--body); color: var(--ink); }
  .abs { position: absolute; }

  /* Header */
  .site-header { position: absolute; left: 0; top: 0; width: 1200px; height: 80px; z-index: 5; }
  .brand { position: absolute; left: 78px; top: 18px; font-family: var(--heading); font-size: 27px; letter-spacing: 2px; color: var(--ink); }
  .brand::before { content: ""; display: inline-block; width: 8px; height: 8px; background: var(--pink); margin-right: 8px; vertical-align: middle; }
  .main-nav { position: absolute; left: 504px; top: 28px; display: flex; gap: 40px; font-size: 14px; letter-spacing: .5px; color: var(--muted); }

  /* Hero */
  .hero-band { position: absolute; left: 0; top: 0; width: 1200px; height: 940px; }
  .hero-art { position: absolute; left: 537px; top: 100px; width: 620px; height: 530px; }
  .hero-title { position: absolute; left: 78px; top: 204px; font-family: var(--heading); font-size: 37px; line-height: 49px; color: var(--ink); font-weight: 400; }
  .hero-sub { position: absolute; left: 78px; top: 376px; font-size: 20px; line-height: 33px; color: var(--muted); }

  /* Lead form card */
  .lead-card { position: absolute; left: 78px; top: 634px; width: 1042px; height: 385px; background: var(--white); border-radius: 8px; box-shadow: 0 10px 40px rgba(40,40,80,.14); overflow: hidden; display: flex; z-index: 3; }
  .lead-intro { width: 464px; height: 100%; background: linear-gradient(135deg, var(--pink) 0%, #9b6bc4 55%, var(--blue) 100%); color: var(--white); padding: 128px 0 0 58px; }
  .lead-intro .eyebrow { font-size: 16px; margin-bottom: 18px; }
  .lead-intro h2 { font-family: var(--heading); font-weight: 400; font-size: 37px; line-height: 51px; }
  .lead-form { position: relative; flex: 1; }
  .field { position: absolute; left: 85px; width: 414px; border: 1px solid var(--line); border-radius: 3px; font-size: 13px; color: var(--muted); padding: 14px 18px; }
  .field-email { top: 60px; height: 46px; }
  .field-site { top: 123px; height: 46px; }
  .field-msg { top: 186px; height: 92px; }
  .send-btn { position: absolute; left: 85px; top: 300px; font-size: 17px; font-weight: 600; letter-spacing: 1px; color: var(--link); display: flex; align-items: center; gap: 10px; }

  /* Intro copy */
  .intro { position: absolute; left: 0; top: 1098px; width: 1200px; text-align: center; font-family: var(--heading); font-size: 28px; line-height: 42px; color: var(--ink); }
  .intro p + p { margin-top: 22px; }
  .intro strong { font-weight: 700; }

  /* Results */
  .results-bg { position: absolute; left: 0; top: 1340px; width: 1200px; height: 1062px; }
  .results-title { position: absolute; left: 0; top: 1670px; width: 1200px; text-align: center; font-family: var(--heading); font-size: 40px; color: var(--white); }
  .browser { position: absolute; left: 235px; top: 1767px; width: 728px; height: 445px; border: 3px solid rgba(255,255,255,.9); border-radius: 12px; }
  .browser-dots { position: absolute; left: 22px; top: 12px; display: flex; gap: 6px; }
  .browser-dots span { width: 18px; height: 18px; border: 2px solid var(--white); border-radius: 50%; }
  .browser-chart { position: absolute; left: 20px; top: 55px; width: 687px; height: 365px; background: var(--white); }
  .slider-arrow { position: absolute; top: 1959px; width: 72px; height: 72px; border-radius: 50%; background: rgba(0,80,140,.18); display: flex; align-items: center; justify-content: center; }
  .slider-prev { left: 80px; }
  .slider-next { left: 1048px; }
  .results-stat { position: absolute; left: 0; top: 2250px; width: 1200px; text-align: center; font-family: var(--heading); font-size: 29px; color: var(--white); }
  .results-note { position: absolute; left: 0; top: 2305px; width: 1200px; text-align: center; font-size: 18px; color: var(--white); }

  /* Testimonials */
  .testimonials { position: absolute; left: 78px; top: 2400px; width: 1042px; height: 600px; background: var(--white); box-shadow: 0 10px 40px rgba(40,40,80,.08); }
  .testimonials h2 { position: absolute; left: 43px; top: 78px; font-family: var(--heading); font-weight: 400; font-size: 36px; line-height: 49px; }
  .quote-mark { position: absolute; left: 325px; top: 82px; }
  .quote-text { position: absolute; left: 325px; top: 150px; width: 740px; font-size: 14.5px; line-height: 26px; color: var(--muted); }
  .quote-author { position: absolute; left: 325px; top: 240px; font-size: 15px; color: var(--link); letter-spacing: .5px; }
  .quote-pager { position: absolute; left: 325px; top: 286px; display: flex; gap: 8px; }
  .quote-pager span { width: 34px; height: 4px; background: #d8d8dc; }
  .quote-pager span:first-child { background: var(--teal); }

  .growth-chart { position: absolute; left: 0; top: 2630px; width: 1200px; height: 660px; }

  .cta { position: absolute; left: 0; top: 2986px; width: 1200px; text-align: center; color: var(--white); }
  .cta h2 { font-family: var(--heading); font-weight: 400; font-size: 44px; }
  .cta p { margin: 20px auto 0; width: 860px; font-size: 19.5px; line-height: 33px; }
  .cta-btn { display: inline-block; margin-top: 24px; width: 208px; height: 52px; line-height: 52px; border-radius: 26px; background: var(--white); color: var(--ink); font-size: 17px; font-weight: 600; letter-spacing: .5px; }

  .site-footer { position: absolute; left: 0; top: 3283px; width: 1200px; height: 75px; background: var(--white); display: flex; justify-content: center; align-items: center; font-size: 14px; color: var(--muted); }
  .site-footer span.sep { margin: 0 16px; }
</style>
</head>
<body>

<svg class="hero-band" viewBox="0 0 1200 940" aria-hidden="true">
  <defs>
    <linearGradient id="heroGrad" x1="0" y1="1" x2="1" y2="0">
      <stop offset="0" stop-color="#f26a96"/>
      <stop offset=".45" stop-color="#c9a3cf"/>
      <stop offset="1" stop-color="#7cc6f5"/>
    </linearGradient>
  </defs>
  <path d="M0 548 C 320 470 720 330 1060 0 L1200 0 L1200 900 C 1000 700 700 660 420 640 C 260 630 120 650 0 690 Z" fill="url(#heroGrad)"/>
</svg>

<header class="site-header">
  <div class="brand">BRIVOLTA</div>
  <nav class="main-nav"><span>RESULTS</span><span>REFERENCES</span></nav>
</header>

<div class="hero-art" role="img" aria-label="Illustration of a person relaxing with a phone in a hanging egg chair, surrounded by chat bubbles"
     style="background: radial-gradient(ellipse at 65% 55%, #ff3b6e 0%, #e85a9a 35%, rgba(90,150,240,.7) 65%, rgba(140,200,245,0) 78%);"></div>

<h1 class="hero-title">French Backlinks<br>on Quality<br>Magazines and Blogs</h1>
<p class="hero-sub">Only quality backlinks help increase<br>your traffic on Quendo.</p>

<section class="lead-card">
  <div class="lead-intro">
    <p class="eyebrow">Trust Flow Target 15–20</p>
    <h2>Information and<br>Rates</h2>
  </div>
  <form class="lead-form">
    <div class="field field-email">Your Email</div>
    <div class="field field-site">Website</div>
    <div class="field field-msg">How Can We Help You</div>
    <div class="send-btn">SEND NOW
      <svg width="20" height="20" viewBox="0 0 20 20" aria-hidden="true"><rect x="1" y="1" width="18" height="18" fill="none" stroke="#1a9fe0" stroke-width="2"/><path d="M5 10h9M10 6l4 4-4 4" fill="none" stroke="#1a9fe0" stroke-width="2"/></svg>
    </div>
  </form>
</section>

<section class="intro">
  <p>Get backlinks on quality sites that have a <strong>high Trust Flow</strong> and<br><strong>increase your traffic</strong> on Quendo.</p>
  <p>We support most themes and write articles. No return link<br>needed. Without engagement.</p>
</section>

<svg class="results-bg" viewBox="0 0 1200 1062" aria-hidden="true">
  <defs>
    <linearGradient id="resGrad" x1="0" y1="0" x2="1" y2="0">
      <stop offset="0" stop-color="#1fa4f4"/>
      <stop offset="1" stop-color="#2ec4ae"/>
    </linearGradient>
  </defs>
  <path d="M0 52 C 120 0 240 10 330 80 C 440 170 560 260 690 200 C 800 150 860 60 930 110 C 1000 160 1090 140 1200 4 L1200 1062 L0 1062 Z" fill="url(#resGrad)"/>
</svg>

<h2 class="results-title">Examples of results obtained with our backlinks</h2>

<div class="browser">
  <div class="browser-dots"><span></span><span></span><span></span></div>
  <svg class="browser-chart" viewBox="0 0 687 365" font-family="Montserrat, sans-serif">
    <rect x="0" y="0" width="687" height="365" fill="#fff"/>
    <rect x="4" y="20" width="62" height="24" fill="#fff" stroke="#ccc"/>
    <text x="12" y="37" font-size="12" font-weight="600" fill="#333">Explorer</text>
    <line x1="66" y1="44" x2="687" y2="44" stroke="#ccc"/>
    <text x="4" y="71" font-size="12" fill="#333">Summary</text>
    <text x="74" y="71" font-size="12" fill="#1a6fc4">Site Usage</text>
    <text x="148" y="71" font-size="12" fill="#1a6fc4">Ecommerce</text>
    <text x="232" y="71" font-size="12" fill="#1a6fc4">AdReach</text>
    <line x1="0" y1="80" x2="687" y2="80" stroke="#ddd"/>
    <rect x="4" y="98" width="76" height="24" fill="#f2f2f2" stroke="#bbb"/>
    <text x="10" y="114" font-size="11" fill="#333">Sessions ▾</text>
    <text x="86" y="114" font-size="11" font-weight="700" fill="#333">vs.</text>
    <text x="110" y="114" font-size="11" fill="#1a6fc4">Select a metric</text>
    <rect x="493" y="98" width="34" height="24" fill="#f2f2f2" stroke="#bbb"/>
    <text x="500" y="114" font-size="11" fill="#333">Day</text>
    <rect x="527" y="98" width="40" height="24" fill="#f2f2f2" stroke="#bbb"/>
    <text x="532" y="114" font-size="11" fill="#333">Week</text>
    <rect x="567" y="98" width="46" height="24" fill="#dcdcdc" stroke="#bbb"/>
    <text x="572" y="114" font-size="11" font-weight="600" fill="#333">Month</text>
    <rect x="622" y="98" width="28" height="24" fill="#e6e6e6" stroke="#bbb"/>
    <rect x="652" y="98" width="28" height="24" fill="#fff" stroke="#bbb"/>
    <circle cx="10" cy="152" r="4" fill="#1a7fc8"/>
    <text x="20" y="156" font-size="11" fill="#333">Sessions</text>
    <text x="8" y="183" font-size="10" fill="#555">30,000</text>
    <text x="8" y="250" font-size="10" fill="#555">15,000</text>
    <line x1="10" y1="188" x2="675" y2="188" stroke="#eee"/>
    <line x1="10" y1="255" x2="675" y2="255" stroke="#eee"/>
    <polygon points="16,305 56,305 94,302 134,300 168,293 208,251 249,226 287,240 325,249 363,249 403,251 444,253 482,258 520,251 558,246 594,237 629,215 665,188 665,308 16,308" fill="#e4f0f9"/>
    <polyline points="16,305 56,305 94,302 134,300 168,293 208,251 249,226 287,240 325,249 363,249 403,251 444,253 482,258 520,251 558,246 594,237 629,215 665,188" fill="none" stroke="#1a7fc8" stroke-width="2.5"/>
    <g fill="#1a7fc8">
      <circle cx="16" cy="305" r="4"/><circle cx="56" cy="305" r="4"/><circle cx="94" cy="302" r="4"/><circle cx="134" cy="300" r="4"/><circle cx="168" cy="293" r="4"/><circle cx="208" cy="251" r="4"/><circle cx="249" cy="226" r="4"/><circle cx="287" cy="240" r="4"/><circle cx="325" cy="249" r="4"/><circle cx="363" cy="249" r="4"/><circle cx="403" cy="251" r="4"/><circle cx="444" cy="253" r="4"/><circle cx="482" cy="258" r="4"/><circle cx="520" cy="251" r="4"/><circle cx="558" cy="246" r="4"/><circle cx="594" cy="237" r="4"/><circle cx="629" cy="215" r="4"/><circle cx="665" cy="188" r="4"/>
    </g>
    <line x1="10" y1="308" x2="675" y2="308" stroke="#bbb"/>
    <g font-size="10" fill="#555">
      <text x="30" y="324">April 2017</text><text x="145" y="324">July 2017</text><text x="255" y="324">October 2017</text><text x="365" y="324">January 2018</text><text x="485" y="324">April 2018</text><text x="598" y="324">July 2018</text>
    </g>
  </svg>
</div>

<div class="slider-arrow slider-prev"><svg width="24" height="24" viewBox="0 0 24 24" aria-hidden="true"><path d="M15 4l-8 8 8 8" fill="none" stroke="#fff" stroke-width="2.5"/></svg></div>
<div class="slider-arrow slider-next"><svg width="24" height="24" viewBox="0 0 24 24" aria-hidden="true"><path d="M9 4l8 8-8 8" fill="none" stroke="#fff" stroke-width="2.5"/></svg></div>

<p class="results-stat">From 0 to 26 000 visits / month</p>
<p class="results-note">And it continues to increase!</p>

<svg class="growth-chart" viewBox="0 0 1200 660" aria-hidden="true">
  <polygon points="0,300 112,295 224,304 325,266 443,284 560,201 672,199 762,148 878,215 936,121 1026,116 1086,31 1160,58 1200,0 1200,660 0,660" fill="#ff3366"/>
  <g fill="#1d1d24" stroke="#fff" stroke-width="3">
    <circle cx="112" cy="295" r="8"/><circle cx="224" cy="304" r="8"/><circle cx="325" cy="266" r="8"/><circle cx="443" cy="284" r="8"/><circle cx="560" cy="201" r="8"/><circle cx="672" cy="199" r="8"/><circle cx="762" cy="148" r="8"/><circle cx="878" cy="215" r="8"/><circle cx="936" cy="121" r="8"/><circle cx="1026" cy="116" r="8"/><circle cx="1086" cy="31" r="8"/><circle cx="1160" cy="58" r="8"/>
  </g>
</svg>

<section class="testimonials" style="height:230px; box-shadow:none; background:transparent;"></section>
<section class="testimonials" style="z-index:0;">
  <h2>Client<br>Testimonials</h2>
  <svg class="quote-mark" width="66" height="52" viewBox="0 0 66 52" aria-hidden="true">
    <path d="M28 4 C 12 8 4 20 4 32 a12 12 0 1 0 12-12 M60 4 C 44 8 36 20 36 32 a12 12 0 1 0 12-12" fill="none" stroke="#1fa4f4" stroke-width="3"/>
  </svg>
  <p class="quote-text">Lorem Ipsum is simply dummy text of the printing and typesetting industry. Lorem Ipsum has been the industry's standard dummy text ever since the 1500s, when an unknown printer took a galley of type and scrambled it to make a type specimen book. It has survived not only five centuries.</p>
  <p class="quote-author">– CLIENT NAME</p>
  <div class="quote-pager"><span></span><span></span><span></span></div>
</section>

<svg class="growth-chart" viewBox="0 0 1200 660" aria-hidden="true" style="z-index:1;">
  <polygon points="0,300 112,295 224,304 325,266 443,284 560,201 672,199 762,148 878,215 936,121 1026,116 1086,31 1160,58 1200,0 1200,660 0,660" fill="#ff3366"/>
  <g fill="#1d1d24" stroke="#fff" stroke-width="3">
    <circle cx="112" cy="295" r="8"/><circle cx="224" cy="304" r="8"/><circle cx="325" cy="266" r="8"/><circle cx="443" cy="284" r="8"/><circle cx="560" cy="201" r="8"/><circle cx="672" cy="199" r="8"/><circle cx="762" cy="148" r="8"/><circle cx="878" cy="215" r="8"/><circle cx="936" cy="121" r="8"/><circle cx="1026" cy="116" r="8"/><circle cx="1086" cy="31" r="8"/><circle cx="1160" cy="58" r="8"/>
  </g>
</svg>

<section class="cta" style="z-index:2;">
  <h2>Information request</h2>
  <p>Would you like more information or pricing? Fill in the short contact form and tell us about your SEO needs and goals. The rates of the backlinks vary according to the theme.</p>
  <span class="cta-btn">CONTACT US</span>
</section>

<footer class="site-footer" style="z-index:2;">
  <span>Home</span><span class="sep">|</span>
  <span>Improve your SEO</span><span class="sep">|</span>
  <span>Socialbay</span><span class="sep">|</span>
  <span>My account</span><span class="sep">|</span>
  <span>Legal Notice</span><span class="sep">|</span>
  <span>About</span><span class="sep">|</span>
  <span>Contact</span>
</footer>

</body>
</html>
```